Aomizu Lodge

We need a web site design for our ski lodge in Japan. We have an older style web site and need a refresh. I'm after a front page and secondary page templates.

Navigation would be same as existing site. Most of the content would be taken and put in the new site.

Most of the information we require is on the existing pages of the older site. www.aomizulodge-stay.com

We have a splash page on the existing site. This would not be the landing page of the new site. The landing should be the actual page.

Niseko is the No. ski resort in Asia ... We are a western styled lodge for either groups or couples and families.

Target Market(s)

Australian and expats living in Asia. Europeans looking for ski holiday in Japan.

Requirements
Must have
• Should be photo rich showing the fun lifestyle aspects of our lodge.
We have a Pagelink Page. Good to have a LIKE link from new website to that ...
https://www.pagelinkhub.com/AomizuLodge

Nice to have
• An availability calendar showing which rooms are free, their nightly rate from Dec 1 to April 1 for each ski season. There are 6 rooms in the lodge.

```html
<!DOCTYPE html>
<html lang="en">
<head>
<meta charset="utf-8">
<title>Aomizu Lodge – Ski Lodge in Hirafu, Niseko</title>
<link href="https://fonts.googleapis.com/css2?family=Arimo:wght@400;700&display=swap" rel="stylesheet">
<style>
:root{
  --blue:#1a78b8;
  --red:#d0121b;
  --text:#555;
  --dark:#333;
  --nav:#2f2f2f;
  --panel:#f0f0f0;
  --footer:#ececec;
  --bottom:#c9c9c9;
  --frame:#6f8596;
}
*{box-sizing:border-box;margin:0;padding:0}
html,body{width:1067px;height:1200px;overflow:hidden}
body{font-family:"Arimo",Arial,sans-serif;color:var(--text);position:relative;background:#dfe7ef}
.scenery{position:absolute;inset:0;background:linear-gradient(180deg,#3d6fa8 0%,#6e94bd 25%,#c7d3df 55%,#e7edf3 75%,#b9c9d8 100%)}
.page{position:absolute;left:100px;top:0;width:867px;height:1011px;background:var(--frame)}
.page-inner{position:absolute;left:7px;top:0;width:853px;height:1011px;background:#fff}
.abs{position:absolute}
/* header */
.header{left:116px;top:0;width:836px;height:78px;background:linear-gradient(90deg,#8ea5bf,#c9d5e2 45%,#dfe6ee);border-radius:0 0 4px 4px}
.brand{left:134px;top:22px;display:flex;align-items:center;gap:10px;color:#fff;font-weight:700;font-size:36px;letter-spacing:-.5px}
.brand-mark{width:22px;height:22px;background:#fff}
.util{right:126px;top:12px;font-size:9.5px;color:#777}
.util span{margin:0 4px}
.call{right:126px;top:45px;font-size:16px;font-weight:700;color:var(--blue)}
.call em{font-style:normal;color:var(--red)}
/* nav */
.nav{left:116px;top:87px;width:836px;height:40px;background:linear-gradient(#3a3a3a,#262626);border-radius:4px;display:flex;align-items:center;justify-content:space-between;padding:0 17px 0 18px;font-size:12px;color:#fff}
.nav .sep{color:#ccc}
/* hero */
.hero{left:116px;top:138px;width:836px;height:315px;background:#e2e2e2;padding:5px}
.hero-photo{width:100%;height:100%;background:linear-gradient(180deg,#8c9aab 0%,#c6cdd6 30%,#eef0f3 60%,#fbfbfc 100%);position:relative}
.hero-line{position:absolute;color:#fff;font-weight:700;font-size:34px;text-shadow:1px 2px 3px rgba(0,0,0,.45)}
.dots{position:absolute;left:15px;bottom:14px;display:flex;gap:9px}
.dots i{width:18px;height:18px;border-radius:3px;background:#7fb5dd}
.dots i:first-child{background:#1a78b8}
/* headings */
.h2{font-size:21px;color:var(--dark);font-weight:400}
.h2 b{font-weight:400;color:var(--blue)}
.photo{border:3px solid #dcdcdc;box-shadow:0 4px 4px -2px rgba(0,0,0,.25)}
.more{font-size:11.5px;font-weight:700;color:var(--red)}
.welcome-text{left:324px;top:510px;width:342px;font-size:11.7px;line-height:20.5px}
.divider{left:128px;top:669px;width:539px;height:1px;background:#ddd}
/* right */
.webcam{left:698px;top:476px;width:240px;height:71px;border:1px solid #ccc;border-radius:3px;background:linear-gradient(#fff,#ededed);display:flex;align-items:center;padding-left:20px;gap:36px}
.cam-icon{width:40px;height:56px}
.webcam-text{font-size:25px;font-weight:700;color:var(--dark);line-height:27px;text-align:right}
.webcam-text em{font-style:normal;color:var(--red)}
.cal{left:698px;top:594px;width:238px;height:201px;background:#1c1c1c;border-radius:2px;padding:4px 7px 7px}
.cal-head{height:24px;display:flex;align-items:center;justify-content:space-between;color:#fff;font-size:11px;font-weight:700}
.cal-arrow{width:16px;height:16px;border-radius:50%;border:1px solid #999;background:#333;position:relative}
.cal-grid{display:grid;grid-template-columns:repeat(7,1fr);background:#d8d8d8;gap:1px;border:1px solid #bbb}
.cal-grid span{height:22.5px;background:#f4f4f4;font-size:9.5px;font-weight:700;color:#222;display:flex;align-items:center;justify-content:center;position:relative}
.cal-grid .dn{background:#e4e4e4;color:#777;font-style:italic;font-weight:400;height:20px}
.cal-grid .o{color:#aaa;font-weight:400}
.cal-grid .today{background:#3f97dc;color:#fff}
.cal-grid .mark::after{content:"";position:absolute;right:3px;top:2px;width:4px;height:4px;border-radius:50%;background:var(--blue)}
.featured{left:699px;top:812px;width:238px;height:180px;background:var(--panel);border-radius:3px;padding:14px 13px 0}
.featured ul{list-style:none;margin-top:10px}
.featured li{position:relative;padding-left:16px;font-size:11.5px;line-height:17px;margin-bottom:5px}
.featured li::before{content:"";position:absolute;left:2px;top:5px;width:6px;height:6px;border-radius:50%;background:var(--red)}
.featured small{font-size:9px}
/* footer */
.footer{left:0;top:1011px;width:1067px;height:136px;background:var(--footer);border-top:2px solid #5b8fb7}
.fcol{font-size:11.3px;color:#555}
.fcol div{height:24.7px}
.social div{display:flex;gap:10px}
.social i{width:14px;height:14px;border-radius:2px;background:#667;display:inline-block}
.news h3{font-size:12px;font-weight:700;color:#1a5f95;letter-spacing:.3px}
.news p{font-size:10.8px;line-height:16px;margin-top:8px;width:210px}
.input{left:529px;top:1110px;width:169px;height:23px;border:1px solid #ccc;border-radius:3px;background:#fff;font-size:10px;font-style:italic;color:#aaa;padding:5px 10px}
.submit{left:707px;top:1110px;width:66px;height:23px;background:#333;border-radius:4px;color:#fff;font-size:11px;font-weight:700;display:flex;align-items:center;justify-content:center}
.bottom{left:0;top:1147px;width:1067px;height:53px;background:var(--bottom);font-size:11px;color:#444}
.bottom a{color:var(--blue);text-decoration:none}
</style>
</head>
<body>
<div class="scenery" role="img" aria-label="Snowy mountain slopes and blue sky behind the page"></div>
<div class="page"><div class="page-inner"></div></div>

<header>
  <div class="abs header" role="img" aria-label="Winter mountain sky banner"></div>
  <div class="abs brand"><span class="brand-mark"></span>Aomizu Lodge</div>
  <div class="abs util">Home<span>|</span>FAQ<span>|</span>Site Map</div>
  <div class="abs call"><em>Call Us:</em> +61 400 555 019</div>
</header>

<nav class="abs nav">
  <span>About Niseko</span><span class="sep">|</span><span>How to Get There</span><span class="sep">|</span><span>Lodge Booking</span><span class="sep">|</span><span>Photo Gallery</span><span class="sep">|</span><span>Snow Report</span><span class="sep">|</span><span>Guest Book</span><span class="sep">|</span><span>Village Map</span><span class="sep">|</span><span>Contact Us</span>
</nav>

<section class="abs hero">
  <div class="hero-photo" role="img" aria-label="Two skiers holding hands on a snowy slope above the village">
    <div class="hero-line" style="left:205px;top:14px">Stay in Comfort,</div>
    <div class="hero-line" style="left:349px;top:56px">Live in Culture,</div>
    <div class="hero-line" style="left:493px;top:98px">Experience the Power.</div>
    <div class="dots"><i></i><i></i><i></i><i></i></div>
  </div>
</section>

<main>
  <h2 class="abs h2" style="left:128px;top:473px"><b>Welcome to</b> Aomizu Lodge</h2>
  <div class="abs photo" style="left:128px;top:516px;width:178px;height:130px;background:linear-gradient(#a9c3e6,#dfe9f7)" role="img" aria-label="Skiers on a groomed run"></div>
  <p class="abs welcome-text">Welcome to Aomizu Lodge in the main ski village of Hirafu. Our hosts will help you experience the endless powder snow! Now's the time to get together and plan your northern hemisphere Japanese ski holiday. We have an average of 13m of snow per season. Located within Hirafu village in Niseko, all 5 ski areas, restaurants &amp; bars are only minutes walk away.</p>
  <div class="abs more" style="left:324px;top:644px">READ MORE</div>
  <div class="abs divider"></div>

  <h2 class="abs h2" style="left:128px;top:684px"><b>Niseko</b> Photo Gallery</h2>
  <div class="abs more" style="left:611px;top:691px">VIEW ALL</div>
  <div class="abs photo" style="left:128px;top:730px;width:168px;height:112px;background:linear-gradient(#cfd3d9,#eceef1)" role="img" aria-label="Skier spraying powder"></div>
  <div class="abs photo" style="left:313px;top:730px;width:169px;height:112px;background:linear-gradient(#e6e8ec,#9a5a5a)" role="img" aria-label="Gondola station with skiers"></div>
  <div class="abs photo" style="left:499px;top:730px;width:167px;height:112px;background:linear-gradient(#b9cfe7,#6f8db3)" role="img" aria-label="Parent teaching a child to ski"></div>
  <div class="abs photo" style="left:128px;top:865px;width:168px;height:112px;background:linear-gradient(#9a4a22,#c98a4a)" role="img" aria-label="Guests enjoying a noodle dinner"></div>
  <div class="abs photo" style="left:313px;top:865px;width:169px;height:112px;background:linear-gradient(#bfc3c9,#eef0f2)" role="img" aria-label="Snowboarder carving through fresh snow"></div>
  <div class="abs photo" style="left:499px;top:865px;width:167px;height:112px;background:linear-gradient(#5a4440,#c88aa6)" role="img" aria-label="Friends celebrating at the lodge"></div>

  <aside>
    <div class="abs webcam">
      <svg class="cam-icon" viewBox="0 0 40 56"><circle cx="20" cy="16" r="13" fill="#555"/><circle cx="20" cy="16" r="6" fill="#ddd"/><rect x="17" y="28" width="6" height="16" fill="#666"/><rect x="8" y="44" width="24" height="6" rx="3" fill="#555"/></svg>
      <div class="webcam-text">View <em>LIVE</em><br>Webcam</div>
    </div>

    <h2 class="abs h2" style="left:698px;top:563px"><b>Availibilty</b> Calendar</h2>
    <div class="abs cal">
      <div class="cal-head">
        <span class="cal-arrow"><svg width="14" height="14" viewBox="0 0 14 14"><path d="M8 4 5 7l3 3z" fill="#fff"/></svg></span>
        <span>April 2013</span>
        <span class="cal-arrow"><svg width="14" height="14" viewBox="0 0 14 14"><path d="M6 4l3 3-3 3z" fill="#fff"/></svg></span>
      </div>
      <div class="cal-grid">
        <span class="dn">Sun</span><span class="dn">Mon</span><span class="dn">Tue</span><span class="dn">Wed</span><span class="dn">Thu</span><span class="dn">Fri</span><span class="dn">Sat</span>
        <span class="o">27</span><span class="o">28</span><span>1</span><span>2</span><span>3</span><span>4</span><span>5</span>
        <span>6</span><span>7</span><span>8</span><span class="mark">9</span><span>10</span><span>11</span><span>12</span>
        <span>13</span><span>14</span><span>15</span><span>16</span><span>17</span><span class="today">18</span><span>19</span>
        <span>20</span><span>21</span><span class="mark">22</span><span>23</span><span>24</span><span>25</span><span>26</span>
        <span>27</span><span>28</span><span>29</span><span>30</span><span>31</span><span class="o">1</span><span class="o">2</span>
        <span class="o">3</span><span class="o">4</span><span class="o">5</span><span class="o">6</span><span class="o">7</span><span class="o">8</span><span class="o">9</span>
      </div>
    </div>

    <div class="abs featured">
      <h2 class="h2"><b>Niseko</b> Featured</h2>
      <ul>
        <li>Located in main ski village of Hirafu.</li>
        <li>2 double / 4 quad rooms.<small>(max 16 per)</small></li>
        <li>Free broadband Internet, big lounge, shared kitchen, separate gender bathrooms.</li>
      </ul>
      <div class="more" style="text-align:right;margin-top:6px">READ MORE</div>
    </div>
  </aside>
</main>

<footer>
  <div class="abs footer"></div>
  <div class="abs fcol" style="left:116px;top:1039px"><div>About Niseko</div><div>How to Get There</div><div>Lodge Booking</div><div>Photo Gallery</div></div>
  <div class="abs fcol" style="left:260px;top:1039px"><div>Snow Report</div><div>Guest Book</div><div>Village Map</div><div>Contact Us</div></div>
  <div class="abs fcol social" style="left:393px;top:1039px"><div><i></i>Pagelink</div><div><i></i>Chirper</div><div><i></i>Circles +</div><div><i></i>ClipTube</div></div>
  <div class="abs news" style="left:528px;top:1033px">
    <h3>NEWSLETTER SUBSCRIBE</h3>
    <p>Get Updates from us please subscribe our Free Newsletter with enter your e- mail address</p>
  </div>
  <div class="abs input">Enter Email</div>
  <div class="abs submit">SUBMIT</div>
  <div class="abs bottom">
    <span class="abs" style="left:116px;top:20px">Copyright © 2013 <a href="#">Aomizu Lodge.com</a>. All Right Reserved</span>
    <span class="abs" style="right:116px;top:20px">All Images &amp; Content Copyright&nbsp; By Aomizu Lodge.com</span>
  </div>
</footer>
</body>
</html>
```